Harbor Bloom Nutraceutical Website

Need a website for a vitamin gummy manufacturing and white-labeling company based in Charleston, SC. We service Zelvorn brands, Ecommerce brands, and any customer needing supplement gummies white labeled. I added out logos for color and style. We have always used navy blue, gold, and white in our color palet, we decided to add purple into the logo.

Our partner's website, that makes caples and powders, is https://www.brelmoxworks.com/

We are just now moving into our facility and don't have pictures or videos of the space, equipement, products, etc. I attached the flyer for the machine we have as reference.

The site just needs to be a simple landing page for now. 'Request Quote' for sales leads and 'enquire here' for job applications. I just need a simple site so we can have our state's dept of commerce announce us publicly.

There are 2 logos. We will be using 'Harbor Bloom Nutraceutical' for now. I cannot use "HB Nutra" until I have approval from our state, but "HB nutra" will be the end logo for use after a couple of months.

```html
<!DOCTYPE html>
<html lang="en">
<head>
<meta charset="utf-8">
<title>Harbor Bloom Nutraceutical — Mobile Landing</title>
<link href="https://fonts.googleapis.com/css2?family=Lexend:wght@300;400;500;600&display=swap" rel="stylesheet">
<style>
  :root{
    --sky:#a6d3ec;
    --navy:#1f2d5c;
    --navy-deep:#16204a;
    --royal:#1c3fc4;
    --light-blue:#8ec8ec;
    --pale-blue:#a9d6f2;
    --ink:#2c3450;
    --muted:#5b637c;
    --paper:#fbfaf7;
    --white:#ffffff;
  }
  *{box-sizing:border-box;margin:0;padding:0}
  html,body{width:1200px;height:900px;overflow:hidden}
  body{background:var(--sky);font-family:"Lexend",sans-serif;color:var(--ink);position:relative}

  .screen{position:absolute;top:30px;width:340px;height:840px;background:var(--paper);border-radius:36px;overflow:hidden;box-shadow:0 18px 40px rgba(20,40,80,.18)}
  .screen--hero{left:45px}
  .screen--about{left:430px}
  .screen--services{left:815px}

  /* header */
  .site-header{height:78px;display:flex;align-items:center;justify-content:space-between;padding:0 26px;background:var(--paper)}
  .brand{font-size:13px;font-weight:500;letter-spacing:.12em;color:var(--navy);line-height:1.2;text-transform:uppercase}
  .header-icons{display:flex;gap:14px;align-items:center}

  /* hero */
  .hero{position:relative;height:762px;background:linear-gradient(180deg,#1b2654 0%,#25336a 45%,#3a4a7e 100%);padding:56px 28px 0;color:var(--white)}
  .hero-photo{position:absolute;inset:0;background:linear-gradient(160deg,rgba(28,63,196,.35) 0%,rgba(22,32,74,.0) 40%,rgba(120,135,170,.35) 100%)}
  .hero-content{position:relative}
  .hero h1{font-size:27px;font-weight:500;line-height:1.3;margin-bottom:18px}
  .hero p{font-size:12px;font-weight:300;line-height:1.75;margin-bottom:26px}
  .btn{display:inline-block;border-radius:30px;font-size:11px;font-weight:500;letter-spacing:.06em;text-transform:uppercase;padding:13px 30px}
  .btn--light{background:var(--white);color:var(--navy)}
  .btn--pale{background:var(--pale-blue);color:var(--navy)}
  .hero-product{position:absolute;left:40px;right:28px;bottom:40px;height:250px;border-radius:18px;background:radial-gradient(ellipse at 50% 60%,#f2a65a 0%,#d9565c 30%,#5a6fb0 65%,rgba(58,74,126,0) 100%)}

  /* about */
  .about-photo{height:290px;background:linear-gradient(180deg,#c9ced3 0%,#8f979e 55%,#e6a23c 80%,#7fb84a 100%)}
  .about-body{padding:26px 26px 0}
  .section-title{font-size:22px;font-weight:500;line-height:1.3;color:var(--navy)}
  .accent{color:var(--light-blue)}
  .body-copy{font-size:11.5px;font-weight:300;line-height:1.75;color:var(--muted);margin:16px 0 22px}
  .featured{padding:26px 26px 0}
  .featured .section-title{margin-bottom:18px}
  .carousel{position:relative}
  .product-card{background:var(--white);border-radius:16px;box-shadow:0 6px 20px rgba(30,45,90,.08);padding:18px 18px 22px;text-align:center}
  .product-photo{height:110px;border-radius:10px;background:linear-gradient(180deg,#e9ebee 0%,#aab0b6 60%,#e9ebee 100%)}
  .product-name{font-size:18px;font-weight:500;color:var(--navy);margin:16px 0 10px}
  .view-all{font-size:13px;color:var(--navy);text-decoration:underline}
  .arrow{position:absolute;top:60px;width:30px;height:30px;border-radius:50%;background:var(--navy);display:flex;align-items:center;justify-content:center}
  .arrow--prev{left:-14px}
  .arrow--next{right:-14px}

  /* services */
  .precision-photo{height:170px;background:linear-gradient(160deg,#5d6670 0%,#9aa3ab 50%,#3c4650 100%)}
  .services-body{padding:24px 26px 0}
  .services-body .section-title + .body-copy{margin-bottom:18px}
  .job-card{margin:6px 18px 0;border-radius:24px;height:150px;background:linear-gradient(135deg,#1566b8 0%,#2c8fd6 60%,#7ec27a 100%);padding:24px 22px;color:var(--white)}
  .job-card h3{font-size:20px;font-weight:500;line-height:1.3}
  .job-card p{font-size:11px;font-weight:300;line-height:1.6;margin-top:8px}

  .brand-tile{position:absolute;left:18px;right:18px;bottom:18px;background:var(--white);border-radius:18px;padding:18px 20px;text-align:center;font-size:22px;font-weight:500;letter-spacing:.08em;color:var(--navy);line-height:1.25;text-transform:uppercase}
</style>
</head>
<body>

  <!-- Home / hero screen -->
  <section class="screen screen--hero">
    <header class="site-header">
      <div class="brand">Harbor Bloom<br>Nutraceutical</div>
      <div class="header-icons">
        <svg width="22" height="22" viewBox="0 0 22 22" aria-label="Search"><circle cx="9" cy="9" r="7" fill="none" stroke="#1f2d5c" stroke-width="2"/><line x1="14" y1="14" x2="20" y2="20" stroke="#1f2d5c" stroke-width="2" stroke-linecap="round"/></svg>
        <svg width="26" height="20" viewBox="0 0 26 20" aria-label="Menu"><g stroke="#1f2d5c" stroke-width="2" stroke-linecap="round"><line x1="6" y1="2" x2="25" y2="2"/><line x1="1" y1="10" x2="25" y2="10"/><line x1="10" y1="18" x2="25" y2="18"/></g></svg>
      </div>
    </header>
    <div class="hero">
      <div class="hero-photo" role="img" aria-label="Gummy production line conveyor in blue light"></div>
      <div class="hero-content">
        <h1>Gummy Production Line and Nutraceutical Manufacturing</h1>
        <p>Sed ut perspiciatis unde omnis iste natus error sit voluptatem accusantium doloremque laudantium, totam rem aperiam, eaque ipsa quae ab illo inventore veritatis et quasi architecto beatae vitae dicta sunt explicabo. Nemo sed quia consequuntur magni dolores eos qui ratione voluptatem sequi nesciunt.</p>
        <a class="btn btn--light">Learn More</a>
      </div>
      <div class="hero-product" role="img" aria-label="Supplement jars with colourful gummies"></div>
    </div>
  </section>

  <!-- About screen -->
  <section class="screen screen--about">
    <div class="about-photo" role="img" aria-label="Gummy depositing machine with gummies and leaves in front"></div>
    <div class="about-body">
      <h2 class="section-title">Gummy Production Line and <span class="accent">Nutraceutical</span> Manufacturing</h2>
      <p class="body-copy">Sed ut perspiciatis unde omnis iste natus error sit voluptatem accusantium doloremque laudantium, totam rem aperiam, eaque ipsa quae ab illo inventore veritatis et quasi architecto beatae vitae dicta sunt explicabo. Nemo enim ipsam voluptatem quia voluptas sit aspernatur aut odit aut fugit, sed quia consequuntur magni dolores eos qui ratione voluptatem sequi nesciunt.</p>
      <a class="btn btn--pale">Request Quote</a>
    </div>
    <div class="featured">
      <h2 class="section-title">Featured Manufacturing</h2>
      <div class="carousel">
        <div class="product-card">
          <div class="product-photo" role="img" aria-label="Stainless steel cooling tunnel machine"></div>
          <div class="product-name">Cooling Tunnel</div>
          <a class="view-all">View all</a>
        </div>
        <span class="arrow arrow--prev"><svg width="10" height="10" viewBox="0 0 10 10"><polyline points="7,1 3,5 7,9" fill="none" stroke="#fff" stroke-width="1.6"/></svg></span>
        <span class="arrow arrow--next"><svg width="10" height="10" viewBox="0 0 10 10"><polyline points="3,1 7,5 3,9" fill="none" stroke="#fff" stroke-width="1.6"/></svg></span>
      </div>
    </div>
  </section>

  <!-- Services screen -->
  <section class="screen screen--services">
    <div class="precision-photo" role="img" aria-label="Close view of production machinery"></div>
    <div class="services-body">
      <h2 class="section-title">Gummy <span class="accent">Manufacturing</span> with Precision</h2>
      <p class="body-copy">Sed ut perspiciatis unde omnis iste natus error sit voluptatem accusantium doloremque laudantium, totam rem aperiam.</p>
      <h2 class="section-title">Services</h2>
      <p class="body-copy">Sed ut perspiciatis unde omnis iste natus error sit voluptatem accusantium doloremque laudantium.</p>
    </div>
    <div class="job-card">
      <h3>Looking for Job Applications?</h3>
      <p>Sed ut perspiciatis unde omnis iste natus error sit voluptatem doloremque.</p>
    </div>
    <div class="brand-tile">Harbor Bloom<br>Nutraceutical</div>
  </section>

</body>
</html>
```